Portfolio site - Need a basic WordPress or SquareSpace site

I need a portfolio site where I have the option to keep updating it on my own. Therefore, I'm guessing I need one that uses WordPress or SquareSpace. I just need a simple and elegant design. I'm a writer (scholarly, fiction and journalism).

Target Market(s)

Adult

Industry/Entity Type

Writer

Number of Pages Required

4 page

Font styles to use
Serif

Colors
b7a5cd
e667a6
85abd2

Requirements
Must have
• Easily updatable features. I'll have to publish links and small blurbs from time to time. And maybe the occasional image.
• Pages should be:
• Home
• Work
• Press
• Contact

```html
<!DOCTYPE html>
<html lang="en">
<head>
<meta charset="utf-8">
<title>Nadira Vell — Writer</title>
<link href="https://fonts.googleapis.com/css2?family=Roboto+Condensed:wght@400;700&family=Open+Sans:wght@400;600&display=swap" rel="stylesheet">
<style>
:root{
  --lavender:#b8a4f2;
  --lavender-soft:#c3b1f5;
  --pink:#f35bd9;
  --pink-bright:#f257f5;
  --pink-text:#f03fc8;
  --blue:#8ec4f2;
  --blue-head:#74b4ee;
  --blue-card:#b9dcf8;
  --ink:#3c3c46;
  --grey:#8a8a94;
  --white:#ffffff;
}
*{margin:0;padding:0;box-sizing:border-box}
html,body{width:1200px;height:3863px;overflow:hidden}
body{position:relative;font-family:"Open Sans",Arial,sans-serif;color:var(--ink);background:var(--white)}
.abs{position:absolute}
.head{font-family:"Roboto Condensed","Arial Narrow",sans-serif;font-weight:700}
section,header,footer{position:absolute;left:0;width:1200px}
.center{left:0;width:1200px;text-align:center}
.kicker{font-family:"Roboto Condensed",sans-serif;font-weight:700;font-size:15px;letter-spacing:.5px;text-transform:uppercase}
.title{font-family:"Roboto Condensed",sans-serif;font-weight:700;font-size:46px;line-height:1;text-transform:uppercase}
.rule{position:absolute;height:1px;background:rgba(255,255,255,.6)}
.small{font-size:11px;line-height:1.6}
.btn{position:absolute;background:var(--pink);color:#fff;font-size:12px;font-weight:600;text-align:center;border-radius:2px}

/* header */
.site-header{top:0;height:134px;border-top:3px solid #eee;background:#fff}
.brand{top:22px;font-family:"Roboto Condensed",sans-serif;font-weight:700;font-size:28px;color:var(--ink)}
.brand-dot{display:inline-block;width:10px;height:10px;border-radius:50%;background:var(--ink);margin-right:8px;vertical-align:middle}
.nav-line{position:absolute;top:103px;height:1px;background:#ccc}
.nav-end{position:absolute;top:96px;width:14px;height:14px;border-radius:50%;background:#555}
.nav a{position:absolute;top:94px;font-size:12px;color:var(--ink);text-decoration:none;text-transform:uppercase}
.nav a.active{color:var(--pink-text);border-bottom:2px solid var(--pink-text);padding-bottom:12px}

/* hero */
.hero{top:134px;height:448px}
.hero-photo{position:absolute;inset:0;background:linear-gradient(180deg,#c9d9e6 0%,#dfe3d6 40%,#a9ae7f 70%,#6f7a45 100%)}
.hero-portrait{position:absolute;left:40px;top:0;width:400px;height:448px;background:radial-gradient(ellipse at 50% 45%,#a57352 0%,#6a4a36 45%,rgba(120,110,80,0) 75%)}
.hero-hi{left:515px;top:146px;font-size:30px;color:var(--pink-text)}
.hero-name{left:515px;top:172px;font-size:58px;color:var(--pink-text);line-height:1}
.hero-sub{left:515px;top:240px;font-size:12px;font-weight:600;color:#333}
.social{position:absolute;top:268px;width:28px;height:28px;border-radius:50%;border:2px solid #444}
.hero-arrow{left:1035px;top:200px}

/* about */
.about{top:582px;height:443px;background:linear-gradient(180deg,var(--lavender) 0%,var(--lavender-soft) 100%);color:#fff}
.contact-item{position:absolute;top:254px;font-size:12px;color:#fff;display:flex;align-items:center;gap:12px}
.contact-icon{width:36px;height:36px;border-radius:50%;border:2px solid rgba(255,255,255,.8);display:flex;align-items:center;justify-content:center}

/* work */
.work{top:1025px;height:649px}
.work-tile{position:absolute}
.work-feature{left:172px;top:208px;width:343px;height:361px;background:linear-gradient(160deg,#a6d0f6,#7fb8ee);color:#fff;text-align:center}

/* blog */
.blog{top:1674px;height:471px;background:var(--blue);color:#fff}
.post{position:absolute;background:var(--blue-card);box-shadow:0 3px 8px rgba(0,0,0,.12);color:#3d5a78}
.post h4{font-family:"Roboto Condensed",sans-serif;font-size:15px;color:#2f5f8c;font-weight:700}
.meta{font-size:8px;color:#6a88a6;margin:4px 0 8px}

/* book */
.book{top:2145px;height:507px}
.book-input{position:absolute;left:172px;top:391px;width:291px;height:37px;background:#f3f3f3;font-size:11px;color:#999;padding:11px 12px}

/* testimonials */
.testimonials{top:2652px;height:374px;background:var(--pink-bright);color:#fff}
.quote{position:absolute;top:150px;width:271px;height:159px;background:#f7a5f8;box-shadow:0 3px 8px rgba(0,0,0,.15);padding:22px 26px;color:#5b2a5c}
.author{display:flex;align-items:center;gap:8px;margin-top:14px;font-size:10px;font-weight:600}
.avatar{width:22px;height:22px;border-radius:50%;background:#c9a88e}

/* experience */
.experience{top:3026px;height:188px;background:var(--lavender);color:#fff}
.years{position:absolute;top:13px;width:162px;height:162px;border-radius:50%;border:4px solid #fff;display:flex;flex-direction:column;align-items:center;justify-content:center;font-family:"Roboto Condensed",sans-serif}

/* press */
.press{top:3214px;height:399px}
.release{position:absolute;top:159px;width:420px;height:160px;background:#fff;box-shadow:0 1px 6px rgba(0,0,0,.08)}

/* footer */
.site-footer{top:3613px;height:250px;background:var(--blue);color:#fff}
.foot-social{position:absolute;top:60px;width:30px;height:30px;border:2px solid #fff}
.foot-nav a{position:absolute;top:120px;font-size:11px;color:#fff;text-decoration:none}
</style>
</head>
<body>

<header class="site-header">
  <div class="abs center brand"><span class="brand-dot"></span>Nadira Vell</div>
  <div class="nav-line" style="left:206px;width:206px"></div>
  <div class="nav-line" style="left:800px;width:204px"></div>
  <span class="nav-end" style="left:178px"></span>
  <span class="nav-end" style="left:1010px"></span>
  <nav class="nav">
    <a class="active" href="#" style="left:443px">Home</a>
    <a href="#" style="left:530px">Work</a>
    <a href="#" style="left:617px">Press</a>
    <a href="#" style="left:706px">Contact</a>
  </nav>
</header>

<section class="hero">
  <div class="hero-photo" role="img" aria-label="Outdoor photo of the writer smiling in a grassy field"></div>
  <div class="hero-portrait"></div>
  <div class="abs head hero-hi">HI, I'M</div>
  <h1 class="abs head hero-name">NADIRA VELL</h1>
  <p class="abs hero-sub">I'M A WRITER (SCHOLARLY, FICTION AND JOURNALISM).</p>
  <span class="social" style="left:515px"></span>
  <span class="social" style="left:549px"></span>
  <span class="social" style="left:583px"></span>
  <span class="social" style="left:617px"></span>
  <svg class="abs hero-arrow" width="22" height="40" viewBox="0 0 22 40"><path d="M4 4 L18 20 L4 36" fill="none" stroke="#bbb" stroke-width="4"/></svg>
</section>

<section class="about">
  <div class="abs center kicker" style="top:66px">Who am I</div>
  <h2 class="abs center title" style="top:92px">About Me</h2>
  <div class="rule" style="left:330px;top:117px;width:150px"></div>
  <div class="rule" style="left:720px;top:117px;width:150px"></div>
  <p class="abs small" style="left:230px;top:144px;width:740px;text-align:center">Nulla sodales sapien ultricies orci scelerisque vestibulum. Integer eget cursus erat, nec luctus nibh. Aenean semper vitae ipsum id maximus. Nulla molestie augue id lorem auctor consequat. Integer congue elit vel dictum placerat. Praesent luctus mi et velit fermentum tempor. Aenean vitae orci mauris. Fusce interdum nunc eget tempor ornare. Suspendisse potenti. Proin id tempus nulla. Fusce bibendum quam.</p>
  <div class="contact-item" style="left:316px">
    <span class="contact-icon"><svg width="16" height="16" viewBox="0 0 16 16"><path d="M4 1 L6 5 L4.5 6.5 Q6 10 9.5 11.5 L11 10 L15 12 L13.5 15 Q6 15 1 2.5 Z" fill="#fff"/></svg></span>111 - 5550 123456</div>
  <div class="contact-item" style="left:486px">
    <span class="contact-icon"><svg width="16" height="12" viewBox="0 0 16 12"><rect x="1" y="1" width="14" height="10" fill="none" stroke="#fff" stroke-width="1.5"/><path d="M1 1 L8 7 L15 1" fill="none" stroke="#fff" stroke-width="1.5"/></svg></span>nadiravell@mailbox.test</div>
  <div class="contact-item" style="left:697px">
    <span class="contact-icon"><svg width="16" height="16" viewBox="0 0 16 16"><circle cx="8" cy="8" r="6.5" fill="none" stroke="#fff" stroke-width="1.5"/><path d="M1.5 8 H14.5 M8 1.5 Q4 8 8 14.5 Q12 8 8 1.5" fill="none" stroke="#fff" stroke-width="1.2"/></svg></span>www.nadiravell.test</div>
  <a class="btn" href="#" style="left:520px;top:340px;width:157px;height:36px;line-height:36px;text-decoration:none">Click here for Details</a>
</section>

<section class="work">
  <div class="abs kicker" style="left:172px;top:80px;color:var(--ink);font-size:13px">Portfolio</div>
  <h2 class="abs title" style="left:172px;top:100px;color:var(--blue-head);font-size:42px">Our Work</h2>
  <p class="abs small" style="left:172px;top:144px;width:640px;color:var(--grey)">Nulla sodales sapien ultricies orci scelerisque vestibulum. Integer eget cursus erat, nec luctus nibh. Aenean semper vitae ipsum id maximus. Nulla molestie augue id lorem auctor consequat. Integer congue elit vel dictum placerat.</p>
  <div class="work-tile work-feature" role="img" aria-label="Open book held in hands, tinted blue">
    <div class="head" style="margin-top:108px;font-size:21px;font-weight:400">Curabitur nec Sapien</div>
    <p class="small" style="width:200px;margin:10px auto 0">Ipsum nec cursus eget, tempor non elit. Nulla gravida dui sed ullamcorper pretium. Suspendisse.</p>
    <div class="btn" style="position:relative;display:inline-block;margin-top:16px;width:124px;height:32px;line-height:32px;font-size:10px">Click here for Details</div>
  </div>
  <div class="work-tile" role="img" aria-label="Giant open book under a stormy sky" style="left:538px;top:208px;width:343px;height:178px;background:linear-gradient(180deg,#5d7078,#9aa8a6 60%,#6b5a44)"></div>
  <div class="work-tile" role="img" aria-label="Hands holding an open book" style="left:901px;top:208px;width:126px;height:178px;background:linear-gradient(160deg,#eef2f4,#d9c2b0)"></div>
  <div class="work-tile" role="img" aria-label="Stack of books outdoors" style="left:538px;top:407px;width:165px;height:162px;background:linear-gradient(180deg,#c6cfa8,#6f7c46)"></div>
  <div class="work-tile" role="img" aria-label="Books and coffee on a wooden table" style="left:724px;top:407px;width:157px;height:162px;background:linear-gradient(160deg,#4f4740,#8d8272)"></div>
  <div class="work-tile" role="img" aria-label="Reading a book with a warm drink" style="left:901px;top:407px;width:126px;height:162px;background:linear-gradient(160deg,#6a4a34,#2f4a6a)"></div>
</section>

<section class="blog">
  <div class="abs center kicker" style="top:56px">Recent Post</div>
  <h2 class="abs center title" style="top:82px;font-size:40px">Blog Entries</h2>
  <div class="rule" style="left:330px;top:102px;width:120px"></div>
  <div class="rule" style="left:750px;top:102px;width:120px"></div>
  <p class="abs small" style="left:250px;top:128px;width:700px;text-align:center">Nulla sodales sapien ultricies orci scelerisque vestibulum. Integer eget cursus erat, nec luctus nibh. Aenean semper vitae ipsum id maximus. Nulla molestie augue id lorem auctor consequat.</p>
  <article class="post" style="left:172px;top:188px;width:415px;height:211px">
    <div class="abs" role="img" aria-label="Reader holding a green book" style="left:21px;top:20px;width:152px;height:170px;background:linear-gradient(180deg,#b2603c,#e7d9cc 55%,#2f8a4e)"></div>
    <div class="abs" style="left:188px;top:44px;width:205px">
      <h4>Curabitur nec sapien dignissim</h4>
      <div class="meta">20 JULY 2018 · POSTED BY ADMIN · 15 COMMENTS</div>
      <p class="small" style="font-size:10px">Nulla sodales sapien ultricies orci scelerisque vestibulum. Integer eget cursus erat, nec luctus nibh. Aenean semper vitae ipsum id maximus. Nulla molestie.</p>
    </div>
  </article>
  <article class="post" style="left:610px;top:188px;width:420px;height:100px">
    <div class="abs" role="img" aria-label="Reader with a book" style="left:10px;top:12px;width:80px;height:76px;background:linear-gradient(160deg,#f2ece6,#c78a5c)"></div>
    <div class="abs" style="left:100px;top:12px;width:300px">
      <h4>Curabitur nec sapien dignissim</h4>
      <div class="meta">20 JULY 2018 · POSTED BY ADMIN · 15 COMMENTS</div>
      <p class="small" style="font-size:10px">Nulla sodales sapien ultricies orci scelerisque vestibulum. Integer eget cursus erat, nec luctus nibh ut.</p>
    </div>
  </article>
  <article class="post" style="left:610px;top:304px;width:420px;height:95px">
    <div class="abs" role="img" aria-label="Cup of coffee on a book" style="left:10px;top:10px;width:80px;height:75px;background:linear-gradient(160deg,#f4f1ec,#6b4a32)"></div>
    <div class="abs" style="left:100px;top:10px;width:300px">
      <h4>Curabitur nec sapien dignissim</h4>
      <div class="meta">20 JULY 2018 · POSTED BY ADMIN · 15 COMMENTS</div>
      <p class="small" style="font-size:10px">Nulla sodales sapien ultricies orci scelerisque vestibulum. Integer eget cursus erat, nec luctus nibh ut.</p>
    </div>
  </article>
</section>

<section class="book">
  <h2 class="abs head" style="left:172px;top:70px;font-size:44px;color:var(--ink)">Experience Book's</h2>
  <div class="abs head" style="left:172px;top:122px;font-size:32px;color:var(--lavender)">First Pages for <span style="color:var(--pink-text)">Free!</span></div>
  <p class="abs small" style="left:172px;top:190px;width:440px;color:var(--grey)">Lorem ipsum dolor sit amet, consectetur adipiscing elit. Morbi a tincidunt tortor. Sed dignissim interdum leo, vel egestas magna ultrices ac.</p>
  <p class="abs small" style="left:172px;top:244px;width:440px;color:var(--grey)">Lorem ipsum dolor sit amet, consectetur adipiscing elit. Morbi a tincidunt tortor. Sed dignissim interdum leo, vel egestas magna ultrices ac. Nunc sapien. Lorem ipsum dolor sit amet, consectetur adipiscing elit. Morbi a tincidunt tortor. Sed dignissim interdum leo, vel egestas magna ultrices ac.</p>
  <p class="abs" style="left:172px;top:328px;width:300px;font-size:16px;color:var(--blue-head);line-height:1.35">Enter your e-mail and get the 1st Chapter for Free</p>
  <div class="book-input">enter your email id</div>
  <div class="btn" style="left:471px;top:391px;width:116px;height:37px;line-height:37px;font-size:13px">Subscribe</div>
  <div class="abs" role="img" aria-label="Open book with fanned pages" style="left:631px;top:185px;width:512px;height:245px;background:radial-gradient(ellipse at 50% 60%,#ffffff 0%,#e4e4e6 45%,#9b9b9f 70%,rgba(255,255,255,0) 72%)"></div>
</section>

<section class="testimonials">
  <div class="abs center kicker" style="top:62px">What People Say</div>
  <h2 class="abs center title" style="top:88px;font-size:40px">Testimonials</h2>
  <div class="rule" style="left:330px;top:108px;width:130px"></div>
  <div class="rule" style="left:740px;top:108px;width:130px"></div>
  <div class="quote" style="left:172px"><p class="small" style="font-size:10px">Lorem ipsum dolor sit amet, consectetur adipiscing elit. Morbi a tincidunt tortor. Sed dignissim interdum leo, vel egestas magna ultrices ac. Nunc sapien.</p><div class="author"><span class="avatar"></span>Daniel Morrow (Australia)</div></div>
  <div class="quote" style="left:466px"><p class="small" style="font-size:10px">Lorem ipsum dolor sit amet, consectetur adipiscing elit. Morbi a tincidunt tortor. Sed dignissim interdum leo, vel egestas magna ultrices ac. Nunc sapien.</p><div class="author"><span class="avatar"></span>Daniel Morrow (Australia)</div></div>
  <div class="quote" style="left:760px"><p class="small" style="font-size:10px">Lorem ipsum dolor sit amet, consectetur adipiscing elit. Morbi a tincidunt tortor. Sed dignissim interdum leo, vel egestas magna ultrices ac. Nunc sapien.</p><div class="author"><span class="avatar"></span>Daniel Morrow (Australia)</div></div>
</section>

<section class="experience">
  <div class="abs kicker" style="left:172px;top:64px;font-size:14px">My Work</div>
  <h2 class="abs title" style="left:172px;top:84px;font-size:38px">Experience</h2>
  <div class="abs" style="left:407px;top:30px;width:1px;height:128px;background:rgba(255,255,255,.5)"></div>
  <div class="years" style="left:498px"><b style="font-size:18px">SCHOLARLY</b><span style="font-size:12px">15 YEARS</span></div>
  <div class="years" style="left:679px"><b style="font-size:18px">FICTION</b><span style="font-size:12px">10 YEARS</span></div>
  <div class="years" style="left:882px"><b style="font-size:18px">JOURNALISM</b><span style="font-size:12px">7 YEARS</span></div>
</section>

<section class="press">
  <div class="abs center kicker" style="top:70px;color:var(--ink)">Press</div>
  <h2 class="abs center title" style="top:94px;color:var(--blue-head);font-size:40px">Release</h2>
  <div class="abs" style="left:330px;top:114px;width:130px;height:1px;background:#ddd"></div>
  <div class="abs" style="left:740px;top:114px;width:130px;height:1px;background:#ddd"></div>
  <article class="release" style="left:172px">
    <div class="abs" role="img" aria-label="Puzzle pieces on a blue table" style="left:21px;top:21px;width:116px;height:121px;background:linear-gradient(160deg,#2f4f8a,#7fa3d8 60%,#3a5d2f)"></div>
    <div class="abs" style="left:152px;top:26px;width:250px"><div style="font-size:14px;color:#444">Vestibulum malesuada metus</div><div style="font-size:12px;font-weight:600;margin:6px 0">22 - 07 - 2018</div><p class="small" style="font-size:10px;color:var(--grey)">Lorem ipsum dolor sit amet, consectetur adipiscing elit. Lorem ipsum dolor sit amet, consectetur adipiscing elit.</p></div>
  </article>
  <article class="release" style="left:610px">
    <div class="abs" role="img" aria-label="Laptop and notebook on a desk" style="left:21px;top:21px;width:116px;height:121px;background:linear-gradient(160deg,#d7d2c8,#4a4540 60%,#8c6a4a)"></div>
    <div class="abs" style="left:152px;top:26px;width:250px"><div style="font-size:14px;color:#444">Vestibulum malesuada metus</div><div style="font-size:12px;font-weight:600;margin:6px 0">22 - 07 - 2018</div><p class="small" style="font-size:10px;color:var(--grey)">Lorem ipsum dolor sit amet, consectetur adipiscing elit. Lorem ipsum dolor sit amet, consectetur adipiscing elit.</p></div>
  </article>
</section>

<footer class="site-footer">
  <div class="rule" style="left:172px;top:75px;width:330px"></div>
  <div class="rule" style="left:698px;top:75px;width:330px"></div>
  <span class="foot-social" style="left:523px"></span>
  <span class="foot-social" style="left:567px"></span>
  <span class="foot-social" style="left:611px"></span>
  <span class="foot-social" style="left:655px"></span>
  <nav class="foot-nav">
    <a href="#" style="left:462px">HOME</a>
    <a href="#" style="left:536px">WORK</a>
    <a href="#" style="left:611px">PRESS</a>
    <a href="#" style="left:684px">CONTACT</a>
  </nav>
  <div class="rule" style="left:172px;top:160px;width:856px"></div>
  <p class="abs center" style="top:178px;font-size:9px">COPYRIGHT © 2018 NADIRA VELL</p>
</footer>

</body>
</html>
```